Ned Farrow & Alan Brisbourne Two Piano Recital

We need a flyer designed to advertise a classical concert featuring pianists Alan Brisbourne & Ned Farrow playing two pianos.

The concert will be held at Kelwood College on Thursday, June 12th at 7:30pm
Supper will be served!
We need something that will get noticed and look cool possibly using the photo attached?

```html
<!DOCTYPE html>
<html lang="en">
<head>
<meta charset="utf-8">
<title>Alan Brisbourne &amp; Ned Farrow – Two Piano Recital</title>
<link rel="stylesheet" href="https://fonts.googleapis.com/css2?family=Cormorant+Garamond:ital,wght@0,400;0,500;0,700;1,400;1,500&family=Libre+Baskerville:wght@700&family=Courier+Prime:wght@700&display=swap">
<style>
  :root {
    --paper: #ffffff;
    --ink: #000000;
    --rule: #8a8a8a;
    --reverse: #ffffff;
    --photo-light: #d9dbdb;
    --photo-mid: #8e9090;
    --photo-dark: #2b2b2b;
  }
  * { margin: 0; padding: 0; box-sizing: border-box; }
  html, body { width: 785px; height: 1200px; overflow: hidden; background: var(--paper); }
  .flyer { position: relative; width: 785px; height: 1200px; background: var(--paper); color: var(--ink); overflow: hidden; }

  .kicker {
    position: absolute; top: 22px; left: 135px; width: 512px;
    text-align: center;
    font-family: "Cormorant Garamond", serif; font-weight: 500;
    font-size: 15px; letter-spacing: 7px;
    padding-bottom: 8px; border-bottom: 1px solid var(--rule);
  }
  .subtitle {
    position: absolute; top: 62px; left: 135px; width: 512px; text-align: center;
    font-family: "Cormorant Garamond", serif; font-weight: 700;
    font-size: 13px; letter-spacing: 3.5px;
  }
  .day {
    position: absolute; top: 136px; left: 238px;
    font-family: "Cormorant Garamond", serif; font-style: italic; font-weight: 400;
    font-size: 38px; letter-spacing: 1px;
  }
  .date {
    position: absolute; top: 182px; left: 146px;
    font-family: "Cormorant Garamond", serif; font-weight: 400;
    font-size: 110px; line-height: 1; letter-spacing: -1px;
  }
  .date sup { font-size: 42px; vertical-align: 52px; letter-spacing: 1px; margin-left: 2px; }
  .time {
    position: absolute; top: 300px; left: 370px;
    font-family: "Cormorant Garamond", serif; font-style: italic; font-weight: 400;
    font-size: 34px;
  }

  .performers { position: absolute; top: 390px; left: 0; width: 785px; height: 272px; background: var(--ink); color: var(--reverse); }
  .ampersand {
    position: absolute; top: -10px; left: 96px;
    font-family: "Cormorant Garamond", serif; font-style: italic; font-weight: 500;
    font-size: 250px; line-height: 1;
  }
  .names {
    position: absolute; top: 50px; left: 285px;
    font-family: "Libre Baskerville", serif; font-weight: 700;
    font-size: 43px; line-height: 70px; letter-spacing: -0.5px; list-style: none;
  }

  .portrait {
    position: absolute; top: 662px; left: 0; width: 785px; height: 426px;
    background: linear-gradient(90deg, var(--photo-light) 0%, var(--photo-mid) 8%, var(--photo-dark) 22%, var(--photo-dark) 40%, var(--photo-light) 55%, var(--photo-mid) 68%, var(--photo-dark) 80%, var(--photo-light) 100%);
  }

  .venue-bar { position: absolute; top: 1088px; left: 0; width: 785px; height: 112px; background: var(--ink); color: var(--reverse); }
  .venue {
    position: absolute; top: 14px; left: 26px;
    font-family: "Courier Prime", monospace; font-weight: 700; font-style: normal;
    font-size: 14.5px; line-height: 20.5px; letter-spacing: 1.8px;
  }
  .supper {
    position: absolute; top: 75px; right: 20px;
    font-family: "Courier Prime", monospace; font-weight: 700;
    font-size: 14.5px; letter-spacing: 1.8px;
  }
</style>
</head>
<body>
<main class="flyer">
  <p class="kicker">LIVE AND IN CONCERT</p>
  <p class="subtitle">PLAYING TWO PIANOS</p>
  <p class="day">THURSDAY</p>
  <p class="date">JUNE 12<sup>TH</sup></p>
  <p class="time">7:30pm</p>

  <section class="performers">
    <span class="ampersand" aria-hidden="true">&amp;</span>
    <ul class="names">
      <li>Alan Brisbourne</li>
      <li>Ned Farrow</li>
    </ul>
  </section>

  <div class="portrait" role="img" aria-label="Halftone photograph of the two pianists standing side by side in waistcoats, shirts and ties"></div>

  <footer class="venue-bar">
    <address class="venue">
      Kelwood College<br>
      Ashcombe Road<br>
      Lindell VIC 310<br>
      P: +61 3.9271.6408
    </address>
    <p class="supper">*Supper will be served</p>
  </footer>
</main>
</body>
</html>
```